Design a sharp Business Card, Stationary, and PowerPoint Template for Harbor Lantern Group (HLG)
Harbor Lantern Group (HLG) is a consulting firm with a mission
Professional
Maren Coleby Ashdown
Managing Director
4870 Larkspur Blvd. NW
Suite 2300
Washington, DC 20417
maren@harborlntn.example
www.harborlntn.example
I'm looking for something sharp that incorporates the colors of the logo.
Business card designs (only), please include this text:
We work with the military, private sector, and nonprofits to protect people affected by conflict and disaster.
This is the logo for Harbor Lantern Group (HLG). The black and red color combo is preferred.
For design purposes, the symbol can be used separately from the text and watermarked.

```html
<!DOCTYPE html>
<html lang="en">
<head>
<meta charset="utf-8">
<title>Harbor Lantern Group — Business Card</title>
<link rel="stylesheet" href="https://fonts.googleapis.com/css2?family=Didact+Gothic&family=Open+Sans:ital,wght@0,400;1,400&display=swap">
<style>
  :root {
    --backdrop: #2a2a2c;
    --card-black: #111112;
    --card-black-edge: #1f1f21;
    --card-white: #f4f4f4;
    --card-white-edge: #dcdcdc;
    --accent-red: #c8262b;
    --ink: #2c2c2c;
    --ink-soft: #5a5a5a;
    --muted: #8a8a8a;
    --paper-white: #ffffff;
  }
  * { box-sizing: border-box; margin: 0; padding: 0; }
  html, body {
    width: 1200px; height: 901px; overflow: hidden;
    background: var(--backdrop);
  }
  .stage { position: relative; width: 1200px; height: 901px; }

  .card {
    position: absolute;
    border-radius: 16px;
    overflow: hidden;
    box-shadow: 0 18px 40px rgba(0,0,0,.45);
  }

  /* Back side */
  .card-back {
    left: 500px; top: 80px; width: 580px; height: 331px;
    background: linear-gradient(135deg, var(--card-black-edge), var(--card-black) 60%);
  }
  .card-back .mark-watermark {
    position: absolute; left: -40px; top: 30px;
    width: 270px; height: 270px; border-radius: 50%;
    background: rgba(255,255,255,.07);
  }
  .card-back .wordmark {
    position: absolute; left: 330px; top: 100px;
    font-family: "Didact Gothic", sans-serif;
    color: var(--paper-white);
    font-size: 24px; line-height: 1.25; letter-spacing: 3px;
    text-transform: uppercase;
  }
  .card-back .web {
    position: absolute; left: 330px; top: 252px;
    font-family: "Open Sans", sans-serif;
    font-size: 11px; letter-spacing: 1.5px; color: var(--muted);
  }

  /* Front side */
  .card-front {
    left: 130px; top: 450px; width: 640px; height: 366px;
    background: linear-gradient(160deg, var(--paper-white), var(--card-white) 55%, var(--card-white-edge));
  }
  .card-front .mark-watermark {
    position: absolute; right: -30px; bottom: -70px;
    width: 320px; height: 320px; border-radius: 50%;
    background: rgba(0,0,0,.05);
  }
  .name-band {
    position: absolute; left: 0; top: 56px; width: 400px; height: 50px;
    background: var(--card-black);
    padding: 6px 0 0 38px;
    font-family: "Open Sans", sans-serif;
  }
  .name-band .person {
    font-style: italic; color: var(--accent-red); font-size: 16px; line-height: 1.2;
  }
  .name-band .role { color: var(--paper-white); font-size: 11px; }

  .front-logo {
    position: absolute; left: 418px; top: 50px;
    display: flex; align-items: center; gap: 14px;
  }
  .front-logo .logo-square {
    width: 48px; height: 48px; border: 2px solid var(--card-black);
  }
  .front-logo .wordmark {
    font-family: "Didact Gothic", sans-serif;
    color: var(--card-black);
    font-size: 17px; line-height: 1.2; letter-spacing: 2.5px;
    text-transform: uppercase;
  }

  .address {
    position: absolute; left: 38px; top: 140px;
    font-family: "Open Sans", sans-serif;
    font-size: 13px; line-height: 1.35; color: var(--ink-soft);
  }
  .contacts {
    position: absolute; left: 38px; top: 210px;
    list-style: none;
    font-family: "Open Sans", sans-serif;
    font-size: 13px; line-height: 1.35; color: var(--ink-soft);
  }
  .contacts li { display: flex; align-items: center; gap: 8px; }
  .contacts svg { width: 12px; height: 12px; fill: var(--accent-red); flex: none; }
  .front-web {
    position: absolute; left: 38px; top: 300px;
    font-family: "Open Sans", sans-serif;
    font-size: 12px; letter-spacing: 1.5px; color: var(--ink);
  }
</style>
</head>
<body>
<main class="stage">

  <section class="card card-back" aria-label="Business card, back">
    <div class="mark-watermark" aria-hidden="true"></div>
    <div class="wordmark">Harbor<br>Lantern<br>Group</div>
    <div class="web">www.harborlntn.example</div>
  </section>

  <section class="card card-front" aria-label="Business card, front">
    <div class="mark-watermark" aria-hidden="true"></div>

    <div class="name-band">
      <div class="person">Maren Coleby Ashdown</div>
      <div class="role">Managing Director</div>
    </div>

    <div class="front-logo">
      <div class="logo-square" aria-hidden="true"></div>
      <div class="wordmark">Harbor<br>Lantern<br>Group</div>
    </div>

    <address class="address" style="font-style:normal">
      4870 Larkspur Blvd. NW<br>
      Suite 2300<br>
      Washington, DC 20417
    </address>

    <ul class="contacts">
      <li>
        <svg viewBox="0 0 12 12" aria-hidden="true"><path d="M1 3c0-1 1-2 2-2h6c1 0 2 1 2 2v1H8V3H4v1H1z M2 5h8l1 6H1z"/></svg>
        202-555-0148
      </li>
      <li>
        <svg viewBox="0 0 12 12" aria-hidden="true"><path d="M3 1h6v10H3z M4 2v6h4V2z"/></svg>
        202-555-0193
      </li>
      <li>
        <svg viewBox="0 0 12 12" aria-hidden="true"><path d="M1 2h10v8H1z M2 3v.6l4 2.8 4-2.8V3z"/></svg>
        maren@harborlntn.example
      </li>
    </ul>

    <div class="front-web">www.harborlntn.example</div>
  </section>

</main>
</body>
</html>
```